business card for horse saddlery

after a new business card for our saddlery, i will add 2 logos we have previously used and they can be used (or not) . Any images can be used from our website also at www.bramwoods.net.au, I have also added our brand logo, which may be good to incorporate on back ? we have over 15, 000 items online, ship Australia Wide.

Target Market(s)

horse owners

Industry/Entity Type

Retail - Equestrian

Contact Information for Business Card

Bramwood Horse Supplies, 1300 62 48 07, www.bramwoods.net.au, 278 Tallowmere Rd Corrindale Q 4602

Requirements
Must have
• ridelark is our brand so ridelark logo on back as 'distributers of', easy to read
Nice to have
• professional but fun
Should not have
• double sided (description wont save double sided)

```html
<!DOCTYPE html>
<html lang="en">
<head>
<meta charset="utf-8">
<title>Bramwood Horse Supplies – Business Card</title>
<link href="https://fonts.googleapis.com/css2?family=Open+Sans:wght@400;600;700;800&display=swap" rel="stylesheet">
<style>
  :root {
    --navy: #0b347a;
    --gold: #fdb61c;
    --white: #ffffff;
    --ink: #2b2f36;
    --backdrop: #1c1c1e;
  }
  * { box-sizing: border-box; margin: 0; padding: 0; }
  html, body { width: 1200px; height: 800px; overflow: hidden; }
  body {
    background: var(--backdrop);
    font-family: "Open Sans", Arial, sans-serif;
    display: flex;
    align-items: center;
    justify-content: center;
    gap: 40px;
  }
  .card {
    width: 560px;
    height: 320px;
    border-radius: 18px;
    position: relative;
    overflow: hidden;
  }

  /* Front */
  .card-front { background: var(--navy); color: var(--white); }
  .brand {
    position: absolute;
    left: 36px;
    top: 118px;
    display: flex;
    align-items: center;
    gap: 14px;
  }
  .brand-dot {
    width: 56px; height: 56px;
    border-radius: 50%;
    background: var(--gold);
    flex: none;
  }
  .brand-name {
    font-weight: 700;
    font-size: 21px;
    line-height: 1.2;
    color: var(--white);
    width: 150px;
  }
  .divider {
    position: absolute;
    left: 268px;
    top: 60px;
    width: 2px;
    height: 200px;
    background: var(--white);
  }
  .contact {
    position: absolute;
    left: 290px;
    top: 62px;
    right: 20px;
  }
  .person-name {
    color: var(--gold);
    font-weight: 800;
    font-size: 25px;
    letter-spacing: 0.5px;
    line-height: 1.1;
  }
  .person-title {
    font-size: 15px;
    font-weight: 600;
    margin-bottom: 12px;
  }
  .contact-list { list-style: none; }
  .contact-item {
    display: flex;
    align-items: flex-start;
    gap: 8px;
    font-size: 13px;
    line-height: 1.35;
    margin-bottom: 4px;
  }
  .contact-item svg { flex: none; width: 13px; height: 13px; margin-top: 3px; fill: var(--gold); }
  .contact-phone { font-weight: 700; font-size: 17px; }
  .contact-phone svg { margin-top: 5px; }

  /* Back */
  .card-back { background: var(--white); }
  .back-band {
    position: absolute;
    left: 0; right: 0; top: 0;
    height: 76px;
    background: var(--gold);
  }
  .back-artwork {
    position: absolute;
    right: 0;
    top: 40px;
    width: 330px;
    height: 280px;
    border-radius: 160px 0 0 0;
    background: linear-gradient(160deg, var(--gold) 0%, #f6e2b4 45%, #dfe6f3 75%, var(--white) 100%);
  }
  .distributor {
    position: absolute;
    left: 30px;
    bottom: 34px;
  }
  .distributor-label {
    color: var(--ink);
    font-weight: 700;
    font-size: 15px;
  }
  .distributor-name {
    color: var(--navy);
    font-weight: 700;
    font-size: 46px;
    letter-spacing: 1px;
    line-height: 1;
  }
</style>
</head>
<body>

  <section class="card card-front" aria-label="Business card front">
    <div class="brand">
      <span class="brand-dot"></span>
      <span class="brand-name">Bramwood Horse Supplies</span>
    </div>
    <div class="divider"></div>
    <div class="contact">
      <p class="person-name">DANIEL HARTLEY</p>
      <p class="person-title">Founder &amp; CEO</p>
      <ul class="contact-list">
        <li class="contact-item">
          <svg viewBox="0 0 24 24" aria-hidden="true"><path d="M12 2a7 7 0 0 0-7 7c0 5 7 13 7 13s7-8 7-13a7 7 0 0 0-7-7zm0 9.5A2.5 2.5 0 1 1 12 6.5a2.5 2.5 0 0 1 0 5z"/></svg>
          <span>278 Tallowmere Rd<br>Corrindale Q 4602</span>
        </li>
        <li class="contact-item contact-phone">
          <svg viewBox="0 0 24 24" aria-hidden="true"><path d="M6.6 10.8a15 15 0 0 0 6.6 6.6l2.2-2.2a1 1 0 0 1 1-.25 11.4 11.4 0 0 0 3.6.57 1 1 0 0 1 1 1V20a1 1 0 0 1-1 1A17 17 0 0 1 3 4a1 1 0 0 1 1-1h3.5a1 1 0 0 1 1 1c0 1.25.2 2.45.57 3.6a1 1 0 0 1-.25 1z"/></svg>
          <span>1300 62 48 07</span>
        </li>
        <li class="contact-item">
          <svg viewBox="0 0 24 24" aria-hidden="true"><path d="M2 5h20v14H2zm2 2v.5l8 5 8-5V7l-8 5z"/></svg>
          <span>office@bramwoods.net.au</span>
        </li>
        <li class="contact-item">
          <svg viewBox="0 0 24 24" aria-hidden="true"><path d="M12 2a10 10 0 1 0 0 20 10 10 0 0 0 0-20zm6.9 9h-3a15 15 0 0 0-1.3-5.6A8 8 0 0 1 18.9 11zM12 4.1c.9 1.2 1.8 3.6 1.9 6.9h-3.8c.1-3.3 1-5.7 1.9-6.9zM9.4 5.4A15 15 0 0 0 8.1 11h-3a8 8 0 0 1 4.3-5.6zM5.1 13h3a15 15 0 0 0 1.3 5.6A8 8 0 0 1 5.1 13zm6.9 6.9c-.9-1.2-1.8-3.6-1.9-6.9h3.8c-.1 3.3-1 5.7-1.9 6.9zm2.6-1.3a15 15 0 0 0 1.3-5.6h3a8 8 0 0 1-4.3 5.6z"/></svg>
          <span>bramwoods.net.au</span>
        </li>
      </ul>
    </div>
  </section>

  <section class="card card-back" aria-label="Business card back">
    <div class="back-band"></div>
    <div class="back-artwork" role="img" aria-label="Large line illustration of a horse head with flowing mane in navy on a gold sun"></div>
    <div class="distributor">
      <p class="distributor-label">Distributers of</p>
      <p class="distributor-name">RIDELARK</p>
    </div>
  </section>

</body>
</html>
```